Award Winning Tourist Attraction Poster

We require a poster for our business which is a tourist attraction called the Brambleton Sands Light Railway. Established in 1948, we are the top tourist attraction iin the area and need a poster that stands out, reflects our corporate identity and appeals to daytrippers and holiday makers. The poster needs to reflect quality.

Our attraction consists of a narrow gauge railway, the world's smallest pub and a cafe.

Target Market(s)

Families primarily, holidaymakers.

Industry/Entity Type

Tourism

Font styles to use
Other font styles liked:
• Gill Sans

Requirements
Must have
• The company colours which are #800000 (Maroon) and 10 C 31 (Ivory) must be incorporated primarily.
• Text and photos as provided - the text must be GILL SANS.
• The logo must be present at the top of the photo
• The poster must be able to work in A3, A4 and A5 sizes
• Show a professional and quality attraction
Should not have
• Clipart
• Flashy text

```html
<!DOCTYPE html>
<html lang="en">
<head>
<meta charset="utf-8">
<title>Brambleton Sands Light Railway – Poster</title>
<link rel="stylesheet" href="https://fonts.googleapis.com/css2?family=Cabin:wght@400;500;700&display=swap">
<style>
  :root {
    --maroon: #800000;
    --maroon-deep: #3a0707;
    --maroon-mid: #5c0f0f;
    --side-red: #8e1a12;
    --side-red-dark: #5a0c08;
    --gold: #f5c518;
    --gold-light: #ffe07a;
    --gold-dark: #c98a0a;
    --ivory: #fffff0;
    --footer: #2a0505;
  }
  * { box-sizing: border-box; margin: 0; padding: 0; }
  html, body { width: 848px; height: 1200px; overflow: hidden; background: #1a0202; }
  .poster {
    position: relative;
    width: 848px;
    height: 1200px;
    overflow: hidden;
    font-family: "Cabin", "Gill Sans", sans-serif;
    background: radial-gradient(ellipse at 30% 40%, var(--side-red) 0%, var(--side-red-dark) 85%);
    color: var(--gold);
    text-align: center;
  }
  .centre-panel {
    position: absolute;
    left: 106px; top: 0;
    width: 636px; height: 1080px;
    background: linear-gradient(90deg, var(--maroon-deep) 0%, var(--maroon-mid) 20%, #6a1410 50%, var(--maroon-mid) 80%, var(--maroon-deep) 100%);
    box-shadow: 0 0 30px rgba(0,0,0,.6);
  }
  .ribbon {
    position: absolute;
    background: linear-gradient(135deg, var(--gold-light), var(--gold) 45%, var(--gold-dark));
    border-radius: 40px 6px 40px 6px;
    box-shadow: 0 4px 10px rgba(0,0,0,.45);
  }
  .ribbon--tl { left: -30px; top: 10px; width: 200px; height: 58px; transform: rotate(18deg); }
  .ribbon--tr { right: -30px; top: 10px; width: 200px; height: 58px; transform: rotate(-18deg); }
  .ribbon--ml { left: 40px; top: 680px; width: 70px; height: 170px; transform: rotate(-20deg); }
  .ribbon--mr { right: 40px; top: 680px; width: 70px; height: 170px; transform: rotate(20deg); }
  .ribbon--bl { left: -30px; bottom: 30px; width: 150px; height: 50px; transform: rotate(25deg); }
  .ribbon--br { right: -30px; bottom: 30px; width: 150px; height: 50px; transform: rotate(-25deg); }
  .brand {
    position: absolute;
    left: 106px; top: 34px; width: 636px;
    font-weight: 700;
    font-size: 44px;
    line-height: 1.12;
    letter-spacing: 2px;
    color: var(--ivory);
    text-transform: uppercase;
  }
  .intro {
    position: absolute;
    left: 106px; top: 240px; width: 636px;
    font-size: 16.5px;
    line-height: 1.48;
  }
  .features {
    position: absolute;
    left: 106px; top: 414px; width: 636px;
  }
  .features .lead { color: var(--ivory); font-size: 15.5px; line-height: 1.45; }
  .features .venue { font-size: 31px; font-weight: 500; line-height: 1.1; text-transform: uppercase; }
  .events {
    margin-top: 2px;
    font-size: 31px; font-weight: 500; line-height: 1.06; text-transform: uppercase;
  }
  .events .and { font-size: 17px; text-transform: none; }
  .photo-strip {
    position: absolute;
    left: 0; top: 880px; width: 848px; height: 200px;
    background: #000;
    display: flex; gap: 8px; padding: 4px 6px;
  }
  .photo { flex: 1; height: 192px; }
  .photo--steam { background: linear-gradient(160deg, #cfd6cf 0%, #4f6a38 45%, #1e2418 80%, #9a958a 100%); }
  .photo--pub { background: linear-gradient(180deg, #9fc2e8 0%, #d9d0c0 45%, #8a3a2a 65%, #5d6a45 100%); }
  .photo--blue { background: linear-gradient(170deg, #a8c58a 0%, #2d4d8c 50%, #1b1b1b 75%, #9a8f80 100%); }
  .photo--black { background: linear-gradient(180deg, #aac7e6 0%, #6e8c4a 45%, #1d1d1d 70%, #8a8378 100%); }
  .contact {
    position: absolute;
    left: 0; top: 1080px; width: 848px; height: 120px;
    background: linear-gradient(180deg, var(--footer), #3d0808);
    color: var(--ivory);
    font-variant: small-caps;
    font-size: 17px;
    line-height: 1.4;
    padding-top: 22px;
    letter-spacing: .5px;
  }
</style>
</head>
<body>
<main class="poster">
  <div class="centre-panel"></div>

  <div class="ribbon ribbon--tl" role="img" aria-label="Gold ribbon decoration"></div>
  <div class="ribbon ribbon--tr" role="img" aria-label="Gold ribbon decoration"></div>
  <div class="ribbon ribbon--ml" role="img" aria-label="Gold ribbon decoration"></div>
  <div class="ribbon ribbon--mr" role="img" aria-label="Gold ribbon decoration"></div>
  <div class="ribbon ribbon--bl" role="img" aria-label="Gold ribbon decoration"></div>
  <div class="ribbon ribbon--br" role="img" aria-label="Gold ribbon decoration"></div>

  <h1 class="brand">Brambleton Sands<br>Light Railway</h1>

  <p class="intro">
    Established in 1948,<br>
    the award-winning Brambleton Sands Light Railway,<br>
    rated the No.1 tourist attraction in North Wexmoor,<br>
    has been delighting old and young alike for generations.<br>
    Sit back and enjoy a 4 mile return journey on one of<br>
    Britain’s oldest seaside miniature railways.<br>
    Celebrating its 10th anniversary with a full refurbishment,
  </p>

  <section class="features">
    <p class="lead">relax with a pint at</p>
    <h2 class="venue">The Lamp Room Inn</h2>
    <p class="lead">the smallest pub on the planet.<br>Why not try</p>
    <h2 class="venue">Station Halt Cafe,</h2>
    <p class="lead">serving delicious breakfasts,<br>light lunches and refreshments.<br>Take part in one of our regular events<br>throughout the year<br>including</p>
    <p class="events">
      Day Out With Captain Puffer,<br>
      Folk &amp; Cider Festival,<br>
      Rail Ale &amp; Blues Festival <span class="and">and</span><br>
      Santa Specials.
    </p>
  </section>

  <section class="photo-strip">
    <div class="photo photo--steam" role="img" aria-label="Photo of a steam locomotive with its driver"></div>
    <div class="photo photo--pub" role="img" aria-label="Photo of guests outside the small station pub"></div>
    <div class="photo photo--blue" role="img" aria-label="Photo of a blue engine at the platform with a guard waving his hat"></div>
    <div class="photo photo--black" role="img" aria-label="Photo of a black locomotive pulling carriages through the countryside"></div>
  </section>

  <footer class="contact">
    <p>Tel: &nbsp;&nbsp;01632 960418</p>
    <p>Email: info@bslr.co.uk</p>
    <p>For more details visit our website at www.bslr.co.uk</p>
  </footer>
</main>
</body>
</html>
```